Lotvantage.com Webpage Design

Design Brief for lotvantage.com (Copy of Brief also in attached Word file)

Name of Website- lotvantage.com (existing logo and look & feel of website to be changed)

Logo - Finalised. The logo files are attached with the brief as “logo.jpeg”. The “Blue- Grey” version of the logo is for use on lighter backgrounds and the “Orange-White” version of the logo is for use on darker backgrounds. (A full Black version of the logo is also attached). Both versions may be used in different parts of the website. All attached files are in .png format.
Status - The website in functional and is undergoing user trials. However, we want to improve the look & feel of the website so at it seems
a. cotemporary,
b. Easy to Navigate
c. professional and
d. Vibrant.

Please visit ‘lotvantage.com’ to check out the website and its functionalities – please use it only as a reference for the features & functions to be provided, however the designer should use a ‘Free Hand’ in designing the composition of various parts of the webpage without getting too influenced by the existing design

Objective of the Website ‘lotvantage.com –
a. It is a portal focussed on listing of ‘Retail’ specific real-estate properties by developers, owners and realty brokers. The properties shall listed under the following four categories-
i. Retail Malls
ii. Shopping Complexes
iii. High-street shops
iv. Retail Warehouses
*refer lotvantage.com for better clarity

b. The abovementioned properties shall be listed either for ‘Sale’ or ‘rent\lease’ or both

c. Users shall visit the site in case they wish to acquire a retail \ shop space either on ‘sale’ or ‘rent’. These Users would be able to specify the ‘Search Criteria’ through the tool-bars provided on the website – the ‘Search Criteria’ shall comprise of ‘Type of space category’, ‘City’, ‘Locality’, transaction type ie ‘Rent \ Sale’ and ‘Area Range’

d. The main revenue model for the website shall be listing fee ( or advertising charges ) payable by those listing their properties on the website.

Three Main Pages of Website (lotvantage.com) that need to be designed -
a. Main Home Page (visit the web link - http://lotvantage.com/ ) - The main home page has the “Search Toolbar” for specifying of Search Criteria by the User. It shall also have the following features & functions-
i. Main Advertising Banner
ii. Featured Projects
iii. New Launches
iv. Toolbar with buttons – ‘Advertise with Us’, ‘Listings Alert’, ‘Lot Mavens’, ‘Advertiser Login’

b. Property Listings Page (visit the web link - http://lotvantage.com/gurgaon-in-india ) - The List of property options that match the Criteria specified by the ‘User’ get displayed on this page.

c. Property Detail Page - When the ‘User’ clicks on the “More….” Button on the ‘Property Listings Page’ (given in point b. above) the web page with the details of the property opens. (For Example – visit the web link - http://lotvantage.com/brevo-Shopping-Complex-brevo-quadrel-gurgaon-636 )

Note:- Please refer to attached ‘Shopping’ related images the designer may use them on the website to provide a look & feel of retail if required – either separately or rotate in a single window

Target Market(s)

Retailers & Investors looking for retail space, Real Estate Brokers, Developers

Industry/Entity Type

Advertising

Number of Pages Required

3 page

Requirements
Must have
• Refer to existing site lotvantage.com -- all the existing functionalities are a must have.
Nice to have
• The Designer may use the retail related images on the website if required for making it more vibrant. Refer attached images Shopping(1-6).jpg

```html
<!DOCTYPE html>
<html lang="en">
<head>
<meta charset="utf-8">
<title>Lotvantage.com – Home</title>
<link href="https://fonts.googleapis.com/css2?family=Roboto+Condensed:wght@400;700&family=Open+Sans:wght@400;600&display=swap" rel="stylesheet">
<style>
:root{
  --navy:#1d2530;
  --panel:#2b323c;
  --panel-dark:#232a33;
  --orange:#f4a523;
  --orange-deep:#f26a10;
  --gold:#f0b54a;
  --gold-light:#f7c863;
  --page:#f4f4f4;
  --line:#dcdcdc;
  --text:#333;
  --footer:#2e3641;
  --footer-bar:#232a33;
  --white:#fff;
}
*{box-sizing:border-box;margin:0;padding:0}
html,body{width:700px;height:1200px;overflow:hidden;background:var(--page)}
body{font-family:"Open Sans",Arial,sans-serif;color:var(--text)}
.canvas{position:relative;width:700px;height:1200px;overflow:hidden;background:var(--page)}
.abs{position:absolute}

/* header */
.site-header{position:absolute;left:0;top:0;width:700px;height:36px;background:var(--navy)}
.brand{position:absolute;left:44px;top:8px;display:flex;align-items:center;gap:5px}
.brand-dot{width:14px;height:14px;border-radius:50%;background:var(--orange)}
.brand-name{font-weight:600;font-size:13px;color:var(--white);white-space:nowrap}
.brand-tag{position:absolute;left:63px;top:24px;font-size:3.6px;color:var(--orange);letter-spacing:.2px;font-weight:600;white-space:nowrap}
.main-nav{position:absolute;top:0;left:314px;height:36px;display:flex}
.main-nav a{display:block;height:36px;line-height:36px;color:var(--white);font-size:10px;text-decoration:none;text-align:center;white-space:nowrap;border-right:1px solid #39424e}
.main-nav a:last-child{border-right:0}
.main-nav a.active{background:var(--orange);border-right:0}

/* hero */
.hero{position:absolute;left:0;top:36px;width:700px;height:389px;
  background:radial-gradient(circle at 63% 42%,#e0c8a8 0,#c9a27a 18%,transparent 40%),
  linear-gradient(180deg,#d8d6d0 0%,#a9a59c 35%,#7a6f62 70%,#5a5046 100%)}
.search-tabs{position:absolute;left:42px;top:156px;display:flex}
.search-tabs span{height:26px;line-height:26px;padding:0 12px;font-family:"Roboto Condensed",sans-serif;font-size:11px}
.tab-sale{background:var(--panel);color:var(--white);width:62px}
.tab-rent{background:#e4e4e4;color:#555;width:62px}
.search-panel{position:absolute;left:42px;top:182px;width:356px;height:139px;background:rgba(35,42,51,.93)}
.check{position:absolute;font-size:7.5px;color:#e6e6e6;display:flex;align-items:center;gap:4px;white-space:nowrap}
.check i{width:8px;height:8px;border:1px solid #bbb;background:#eee;display:inline-block}
.field-label{position:absolute;font-size:7.5px;color:#e6e6e6;white-space:nowrap}
.select{position:absolute;width:160px;height:20px;background:#d9d9d9;border:1px solid #bdbdbd}
.select svg{position:absolute;right:6px;top:7px}
.input{position:absolute;width:160px;height:20px;background:#d9d9d9;border:1px solid #bdbdbd}
.btn-search{position:absolute;left:188px;top:102px;width:78px;height:20px;background:var(--orange-deep);border:1px solid #fff;color:var(--white);font-size:8px;text-align:center;line-height:18px}
.adv-link{position:absolute;left:287px;top:106px;font-size:8px;color:var(--white);white-space:nowrap}

/* sidebar */
.side-block{position:absolute;left:42px;width:144px;background:var(--panel)}
.side-title{height:27px;line-height:28px;padding-left:6px;background:var(--navy);font-family:"Roboto Condensed",sans-serif;font-size:12px;color:var(--white)}
.side-item{position:relative;height:26px;border-top:1px solid #1f252d;font-size:8px;color:var(--white);padding-left:24px;line-height:26px}
.side-item svg.pin{position:absolute;left:8px;top:7px}
.side-item svg.chev{position:absolute;right:10px;top:9px}
.side-item.active{background:var(--panel-dark);color:var(--orange)}
.mavens{position:absolute;left:42px;top:793px;width:144px;height:230px;background:var(--gold)}
.mavens h3{height:31px;line-height:31px;text-align:center;font-family:"Roboto Condensed",sans-serif;font-weight:400;font-size:14px;color:var(--white);background:linear-gradient(180deg,var(--gold-light),var(--gold))}
.mavens p{font-size:7.6px;line-height:10.5px;text-align:center;color:#2a2a2a;padding:4px 6px 0}
.mv-field{position:absolute;left:5px;width:134px;background:#fdf3dc;border:1px solid #e5c47c;font-size:7.5px;color:#aaa;padding:5px}
.mv-submit{position:absolute;left:77px;top:205px;width:60px;height:16px;background:var(--navy);color:var(--white);font-size:8px;text-align:center;line-height:16px}

/* content */
.section-title{position:absolute;left:202px;width:461px;font-family:"Roboto Condensed",sans-serif;font-weight:400;font-size:14px;color:var(--orange);border-bottom:1px solid var(--line);padding-bottom:5px}
.section-title small{font-size:8px;color:#333}
.card{position:absolute;width:142px;height:160px;background:var(--white);border:1px solid #e0e0e0}
.card-media{position:absolute;left:3px;top:4px;width:134px;height:105px;
  background:radial-gradient(ellipse at 50% 38%,#d9a548 0,#8a6a4a 22%,transparent 45%),linear-gradient(180deg,#2e3c63 0%,#4a5a80 40%,#6e7891 70%,#3a3f4c 100%)}
.card-media.alt{background:linear-gradient(180deg,#6fa0d4 0%,#b8c9d8 35%,#8c7c72 60%,#4a4642 100%)}
.card-media.bright{background:linear-gradient(180deg,#b7cde6 0%,#d9dfe4 45%,#a0a6ab 75%,#6e7378 100%)}
.card-cap{position:absolute;left:0;bottom:0;width:100%;height:29px;background:rgba(30,36,46,.72);text-align:center;color:var(--white)}
.card-cap b{display:block;font-family:"Roboto Condensed",sans-serif;font-weight:400;font-size:10.5px;line-height:13px;margin-top:2px}
.card-cap span{display:block;font-size:7.5px;line-height:10px}
.card-text{position:absolute;left:0;top:113px;width:100%;text-align:center;font-size:7.5px;line-height:12px;color:#333}
.card-btn{position:absolute;left:45px;top:139px;width:50px;height:12px;background:var(--orange);color:var(--white);font-size:5.6px;text-align:center;line-height:12px}

/* footer */
.site-footer{position:absolute;left:0;top:1052px;width:700px;height:126px;background:var(--footer)}
.ft-head{position:absolute;font-family:"Roboto Condensed",sans-serif;font-weight:700;font-size:9.5px;color:var(--orange)}
.ft-line{position:absolute;font-size:6.5px;color:#d8dadd;line-height:13px;white-space:nowrap}
.ft-links{position:absolute;font-size:6.5px;color:#d8dadd;line-height:13px;list-style:none;white-space:nowrap}
.ft-links li::before{content:"›";color:var(--orange);margin-right:4px}
.news-box{position:absolute;left:521px;top:1085px;width:144px;height:17px;background:var(--white);border:1px solid #ccc}
.news-box span{position:absolute;left:6px;top:3px;font-size:6.5px;color:#bbb}
.news-btn{position:absolute;right:1px;top:1px;width:43px;height:13px;background:var(--orange);font-size:7px;text-align:center;line-height:13px;color:#222}
.social{position:absolute;width:27px;height:27px;border-radius:50%;background:var(--orange);border:2px solid var(--white)}
.social.first{background:#3c5a99}
.footer-bar{position:absolute;left:0;top:1178px;width:700px;height:22px;background:var(--footer-bar);text-align:center;font-size:6.5px;line-height:22px;color:#e6e6e6}
</style>
</head>
<body>
<div class="canvas">

  <header class="site-header">
    <div class="brand"><span class="brand-dot"></span><span class="brand-name">lotvantage.com</span></div>
    <div class="brand-tag">SHOP SPACES LISTED NATIONWIDE FOR YOU</div>
    <nav class="main-nav">
      <a class="active" href="#" style="width:47px">Home</a>
      <a href="#" style="width:88px">Advertise with Us</a>
      <a href="#" style="width:71px">Listings Alert</a>
      <a href="#" style="width:66px">Lot Mavens</a>
      <a href="#" style="width:84px">Advertiser Login</a>
    </nav>
  </header>

  <section class="hero" role="img" aria-label="Banner photo: a joyful shopper in a bright orange top holding colourful shopping bags inside a mall"></section>

  <div class="search-tabs"><span class="tab-sale">For Sale</span><span class="tab-rent">For Rent</span></div>
  <form class="search-panel">
    <label class="check" style="left:11px;top:29px"><i></i>Retail Malls</label>
    <label class="check" style="left:73px;top:29px"><i></i>Shopping Complex</label>
    <label class="check" style="left:188px;top:29px"><i></i>High Street Shops</label>
    <label class="check" style="left:267px;top:29px"><i></i>Retail Warehouses</label>
    <span class="field-label" style="left:11px;top:54px">Select City:</span>
    <span class="field-label" style="left:187px;top:54px">Select Locality/Micro-Market.</span>
    <div class="select" style="left:11px;top:63px"><svg width="9" height="6" viewBox="0 0 9 6"><path d="M1 1l3.5 3.5L8 1" fill="none" stroke="#666" stroke-width="1.3"/></svg></div>
    <div class="select" style="left:186px;top:63px"><svg width="9" height="6" viewBox="0 0 9 6"><path d="M1 1l3.5 3.5L8 1" fill="none" stroke="#666" stroke-width="1.3"/></svg></div>
    <span class="field-label" style="left:11px;top:88px">Enter Keywords:</span>
    <div class="input" style="left:11px;top:102px"></div>
    <div class="btn-search">SEARCH</div>
    <span class="adv-link">Advance Search</span>
  </form>

  <aside class="side-block" style="top:397px">
    <div class="side-title">SEARCH BY CATEGORIES</div>
    <div class="side-item"><svg class="pin" width="9" height="12" viewBox="0 0 9 12"><path d="M4.5 0a4.5 4.5 0 0 0-4.5 4.5C0 8 4.5 12 4.5 12S9 8 9 4.5A4.5 4.5 0 0 0 4.5 0z" fill="#7e858e"/><circle cx="4.5" cy="4.5" r="1.6" fill="#2b323c"/></svg>Retail Malls<svg class="chev" width="6" height="9" viewBox="0 0 6 9"><path d="M1 1l3.5 3.5L1 8" fill="none" stroke="#7e858e" stroke-width="1.4"/></svg></div>
    <div class="side-item active"><svg class="pin" width="9" height="12" viewBox="0 0 9 12"><path d="M4.5 0a4.5 4.5 0 0 0-4.5 4.5C0 8 4.5 12 4.5 12S9 8 9 4.5A4.5 4.5 0 0 0 4.5 0z" fill="#f4a523"/><circle cx="4.5" cy="4.5" r="1.6" fill="#232a33"/></svg>Shopping Complexes<svg class="chev" width="6" height="9" viewBox="0 0 6 9"><path d="M1 1l3.5 3.5L1 8" fill="none" stroke="#f4a523" stroke-width="1.6"/></svg></div>
    <div class="side-item"><svg class="pin" width="9" height="12" viewBox="0 0 9 12"><path d="M4.5 0a4.5 4.5 0 0 0-4.5 4.5C0 8 4.5 12 4.5 12S9 8 9 4.5A4.5 4.5 0 0 0 4.5 0z" fill="#7e858e"/><circle cx="4.5" cy="4.5" r="1.6" fill="#2b323c"/></svg>High-street Shops<svg class="chev" width="6" height="9" viewBox="0 0 6 9"><path d="M1 1l3.5 3.5L1 8" fill="none" stroke="#7e858e" stroke-width="1.4"/></svg></div>
    <div class="side-item"><svg class="pin" width="9" height="12" viewBox="0 0 9 12"><path d="M4.5 0a4.5 4.5 0 0 0-4.5 4.5C0 8 4.5 12 4.5 12S9 8 9 4.5A4.5 4.5 0 0 0 4.5 0z" fill="#7e858e"/><circle cx="4.5" cy="4.5" r="1.6" fill="#2b323c"/></svg>Retail &nbsp;Warehouses<svg class="chev" width="6" height="9" viewBox="0 0 6 9"><path d="M1 1l3.5 3.5L1 8" fill="none" stroke="#7e858e" stroke-width="1.4"/></svg></div>
  </aside>

  <aside class="side-block" style="top:540px">
    <div class="side-title">SEARCH BY LOCATION</div>
    <div class="side-item" style="height:27px"><svg class="pin" width="9" height="12" viewBox="0 0 9 12"><path d="M4.5 0a4.5 4.5 0 0 0-4.5 4.5C0 8 4.5 12 4.5 12S9 8 9 4.5A4.5 4.5 0 0 0 4.5 0z" fill="#7e858e"/><circle cx="4.5" cy="4.5" r="1.6" fill="#2b323c"/></svg>Bangalore<svg class="chev" width="6" height="9" viewBox="0 0 6 9"><path d="M1 1l3.5 3.5L1 8" fill="none" stroke="#7e858e" stroke-width="1.4"/></svg></div>
    <div class="side-item active" style="height:27px"><svg class="pin" width="9" height="12" viewBox="0 0 9 12"><path d="M4.5 0a4.5 4.5 0 0 0-4.5 4.5C0 8 4.5 12 4.5 12S9 8 9 4.5A4.5 4.5 0 0 0 4.5 0z" fill="#f4a523"/><circle cx="4.5" cy="4.5" r="1.6" fill="#232a33"/></svg>Chennai<svg class="chev" width="6" height="9" viewBox="0 0 6 9"><path d="M1 1l3.5 3.5L1 8" fill="none" stroke="#f4a523" stroke-width="1.6"/></svg></div>
    <div class="side-item" style="height:27px"><svg class="pin" width="9" height="12" viewBox="0 0 9 12"><path d="M4.5 0a4.5 4.5 0 0 0-4.5 4.5C0 8 4.5 12 4.5 12S9 8 9 4.5A4.5 4.5 0 0 0 4.5 0z" fill="#7e858e"/><circle cx="4.5" cy="4.5" r="1.6" fill="#2b323c"/></svg>Greater Noida<svg class="chev" width="6" height="9" viewBox="0 0 6 9"><path d="M1 1l3.5 3.5L1 8" fill="none" stroke="#7e858e" stroke-width="1.4"/></svg></div>
    <div class="side-item" style="height:27px"><svg class="pin" width="9" height="12" viewBox="0 0 9 12"><path d="M4.5 0a4.5 4.5 0 0 0-4.5 4.5C0 8 4.5 12 4.5 12S9 8 9 4.5A4.5 4.5 0 0 0 4.5 0z" fill="#7e858e"/><circle cx="4.5" cy="4.5" r="1.6" fill="#2b323c"/></svg>Gurgaon<svg class="chev" width="6" height="9" viewBox="0 0 6 9"><path d="M1 1l3.5 3.5L1 8" fill="none" stroke="#7e858e" stroke-width="1.4"/></svg></div>
    <div class="side-item" style="height:28px"><svg class="pin" width="9" height="12" viewBox="0 0 9 12"><path d="M4.5 0a4.5 4.5 0 0 0-4.5 4.5C0 8 4.5 12 4.5 12S9 8 9 4.5A4.5 4.5 0 0 0 4.5 0z" fill="#7e858e"/><circle cx="4.5" cy="4.5" r="1.6" fill="#2b323c"/></svg>Hyderabad<svg class="chev" width="6" height="9" viewBox="0 0 6 9"><path d="M1 1l3.5 3.5L1 8" fill="none" stroke="#7e858e" stroke-width="1.4"/></svg></div>
    <div class="side-item" style="height:27px"><svg class="pin" width="9" height="12" viewBox="0 0 9 12"><path d="M4.5 0a4.5 4.5 0 0 0-4.5 4.5C0 8 4.5 12 4.5 12S9 8 9 4.5A4.5 4.5 0 0 0 4.5 0z" fill="#7e858e"/><circle cx="4.5" cy="4.5" r="1.6" fill="#2b323c"/></svg>Jaipur<svg class="chev" width="6" height="9" viewBox="0 0 6 9"><path d="M1 1l3.5 3.5L1 8" fill="none" stroke="#7e858e" stroke-width="1.4"/></svg></div>
    <div class="side-item" style="height:26px"><svg class="pin" width="9" height="12" viewBox="0 0 9 12"><path d="M4.5 0a4.5 4.5 0 0 0-4.5 4.5C0 8 4.5 12 4.5 12S9 8 9 4.5A4.5 4.5 0 0 0 4.5 0z" fill="#7e858e"/><circle cx="4.5" cy="4.5" r="1.6" fill="#2b323c"/></svg>Khanna<svg class="chev" width="6" height="9" viewBox="0 0 6 9"><path d="M1 1l3.5 3.5L1 8" fill="none" stroke="#7e858e" stroke-width="1.4"/></svg></div>
    <div class="side-item" style="height:28px"><svg class="pin" width="9" height="12" viewBox="0 0 9 12"><path d="M4.5 0a4.5 4.5 0 0 0-4.5 4.5C0 8 4.5 12 4.5 12S9 8 9 4.5A4.5 4.5 0 0 0 4.5 0z" fill="#7e858e"/><circle cx="4.5" cy="4.5" r="1.6" fill="#2b323c"/></svg>Kolkatta<svg class="chev" width="6" height="9" viewBox="0 0 6 9"><path d="M1 1l3.5 3.5L1 8" fill="none" stroke="#7e858e" stroke-width="1.4"/></svg></div>
  </aside>

  <section class="mavens">
    <h3>Lot Mavens</h3>
    <p>Post your Retail Space requirement with usand our experts shall get back with suitableoptions and even help you in your transaction. This is a Free Service!</p>
    <div class="mv-field" style="top:90px;height:22px">Enter your email address</div>
    <div class="mv-field" style="top:118px;height:22px">Mobile No</div>
    <div class="mv-field" style="top:146px;height:54px">Add Description of Requirement</div>
    <div class="mv-submit">SUBMIT</div>
  </section>

  <h2 class="section-title" style="top:438px">Featured Retail Projects <small>Across India</small></h2>

  <article class="card" style="left:202px;top:470px"><div class="card-media" role="img" aria-label="Night photo of a glass shopping complex"><div class="card-cap"><b>Bangalore</b><span>Shopping Complex</span></div></div><div class="card-text">Kessa 81 High Street<br>Sector-81</div><div class="card-btn">View Details</div></article>
  <article class="card" style="left:361px;top:470px"><div class="card-media alt" role="img" aria-label="Daytime photo of a modern retail building with palm trees"><div class="card-cap"><b>Chennai</b><span>Shopping Complex</span></div></div><div class="card-text">Kessa 81 High Street<br>Sector-81</div><div class="card-btn">View Details</div></article>
  <article class="card" style="left:521px;top:470px"><div class="card-media bright" role="img" aria-label="Rendering of a white commercial complex"><div class="card-cap"><b>Hyderabad</b><span>Shopping Complex</span></div></div><div class="card-text">Kessa 81 High Street<br>Sector-81</div><div class="card-btn">View Details</div></article>

  <article class="card" style="left:202px;top:642px"><div class="card-media" role="img" aria-label="Night photo of a glass shopping complex"><div class="card-cap"><b>Bangalore</b><span>Shopping Complex</span></div></div><div class="card-text">Kessa 81 High Street<br>Sector-81</div><div class="card-btn">View Details</div></article>
  <article class="card" style="left:361px;top:642px"><div class="card-media" role="img" aria-label="Night photo of a glass shopping complex"><div class="card-cap"><b>Hyderabad</b><span>Shopping Complex</span></div></div><div class="card-text">Kessa 81 High Street<br>Sector-81</div><div class="card-btn">View Details</div></article>
  <article class="card" style="left:521px;top:642px"><div class="card-media" role="img" aria-label="Night photo of a glass shopping complex"><div class="card-cap"><b>Bangalore</b><span>Shopping Complex</span></div></div><div class="card-text">Kessa 81 High Street<br>Sector-81</div><div class="card-btn">View Details</div></article>

  <h2 class="section-title" style="top:825px">Featured New Launches <small>Across India</small></h2>

  <article class="card" style="left:202px;top:861px"><div class="card-media" role="img" aria-label="Night photo of a glass shopping complex"><div class="card-cap"><b>Bangalore</b><span>Shopping Complex</span></div></div><div class="card-text">Kessa 81 High Street<br>Sector-81</div><div class="card-btn">View Details</div></article>
  <article class="card" style="left:361px;top:861px"><div class="card-media" role="img" aria-label="Night photo of a glass shopping complex"><div class="card-cap"><b>Bangalore</b><span>Shopping Complex</span></div></div><div class="card-text">Kessa 81 High Street<br>Sector-81</div><div class="card-btn">View Details</div></article>
  <article class="card" style="left:521px;top:861px"><div class="card-media" role="img" aria-label="Night photo of a glass shopping complex"><div class="card-cap"><b>Bangalore</b><span>Shopping Complex</span></div></div><div class="card-text">Kessa 81 High Street<br>Sector-81</div><div class="card-btn">View Details</div></article>

  <footer class="site-footer"></footer>
  <h4 class="ft-head" style="left:44px;top:1067px">ADDRESS</h4>
  <svg class="abs" style="left:44px;top:1085px" width="8" height="8" viewBox="0 0 8 8"><path d="M4 0L0 4h1v4h2V5h2v3h2V4h1z" fill="#f4a523"/></svg>
  <div class="ft-line" style="left:57px;top:1085px;line-height:10px">Marketline Realty<br>Block C, Lakeview Road - 560099</div>
  <svg class="abs" style="left:44px;top:1115px" width="8" height="6" viewBox="0 0 8 6"><rect width="8" height="6" fill="#f4a523"/><path d="M0 0l4 3 4-3" fill="none" stroke="#2e3641" stroke-width=".8"/></svg>
  <div class="ft-line" style="left:57px;top:1112px">info@lotvantage.com</div>
  <svg class="abs" style="left:44px;top:1128px" width="8" height="8" viewBox="0 0 8 8"><path d="M1 0h2l1 2-1 1c.5 1 1 1.5 2 2l1-1 2 1v2c-4 0-7-3-7-7z" fill="#f4a523"/></svg>
  <div class="ft-line" style="left:57px;top:1126px">000 000-0000</div>
  <svg class="abs" style="left:44px;top:1144px" width="8" height="8" viewBox="0 0 8 8"><rect x="0" y="2" width="8" height="4" fill="#f4a523"/><rect x="2" y="0" width="4" height="2" fill="#f4a523"/><rect x="2" y="6" width="4" height="2" fill="#f4a523"/></svg>
  <div class="ft-line" style="left:57px;top:1142px">000-000-0000</div>

  <h4 class="ft-head" style="left:203px;top:1067px">MORE LINK</h4>
  <ul class="ft-links" style="left:203px;top:1086px"><li>There are many</li><li>Variations of passages</li><li>Lorem Ipsum</li><li>Suffered alteration</li><li>Injected humour</li><li>Randomised words</li></ul>
  <ul class="ft-links" style="left:301px;top:1086px"><li>There are many</li><li>Variations of passages</li><li>Lorem Ipsum</li><li>Suffered alteration</li><li>Injected humour</li><li>Randomised words</li></ul>
  <ul class="ft-links" style="left:397px;top:1086px"><li>There are many</li><li>Variations of passages</li><li>Lorem Ipsum</li><li>Suffered alteration</li><li>Injected humour</li><li>Randomised words</li></ul>

  <h4 class="ft-head" style="left:521px;top:1068px">NEWSLETTER</h4>
  <div class="news-box"><span>Email address</span><div class="news-btn">Subscribe</div></div>
  <h4 class="ft-head" style="left:521px;top:1113px">CONNECT WITH US</h4>
  <span class="social first" style="left:522px;top:1132px"></span>
  <span class="social" style="left:555px;top:1132px"></span>
  <span class="social" style="left:587px;top:1132px"></span>
  <span class="social" style="left:620px;top:1132px"></span>

  <div class="footer-bar">COPYRIGHT © 2013 MARKETLINE REALTY.COM. ALL RIGHTS RESERVED.</div>
</div>
</body>
</html>
```